UK vitamin company needs a packaging label design for new vitamin range

We have a logo, and we have the product. We now need some beautiful labels to go on the boxes which bring the product range to life.
We have 7 categories: Joint Care, Heart Heath, Brain Function, Immune System, Skin, Antioxidants and Probiotics. Each of these categories should have its own look within the plucky vitamin range. This can be quite subtle, but needs to be clearly visible and should be linked to the category e.g. 'Heart Health' might have a heart etc.
I have uploaded the logo, an example of the pack shape, and the sizing info for the label.
We are a fun brand, so please have some fun with this. We want the labels to be bold, and differentiated from the rest of the category.
Thanks
All images used must be 'rights free'. Many thanks
UK
It Company

```html
<!DOCTYPE html>
<html lang="en">
<head>
<meta charset="utf-8">
<title>Plucky Vitamin – Heart Health Label</title>
<link rel="stylesheet" href="https://fonts.googleapis.com/css2?family=Oswald:wght@500;600&family=Roboto+Condensed:wght@400;700&display=swap">
<style>
  :root {
    --page: #ffffff;
    --label: #ffffff;
    --green: #1f9a45;
    --green-deep: #137a34;
    --orange: #ef7a1c;
    --grey: #9a9a9a;
    --text-light: #ffffff;
    --badge: #3aa549;
    --illus-dark: #2b2e33;
    --illus-red: #d1381c;
  }
  * { box-sizing: border-box; margin: 0; padding: 0; }
  html, body {
    width: 1200px;
    height: 1195px;
    overflow: hidden;
    background: var(--page);
  }
  .canvas {
    position: relative;
    width: 1200px;
    height: 1195px;
  }
  .label {
    position: absolute;
    left: 220px;
    top: 108px;
    width: 760px;
    height: 980px;
    background: var(--label);
    overflow: hidden;
    box-shadow: 0 0 0 1px #eeeeee;
  }
  .label-swoosh {
    position: absolute;
    inset: 0;
    width: 760px;
    height: 980px;
  }
  .brand {
    position: absolute;
    left: 60px;
    top: 92px;
    font-family: "Oswald", sans-serif;
    font-weight: 600;
    font-size: 46px;
    line-height: 1;
    color: var(--green);
  }
  .pack-info {
    position: absolute;
    right: 48px;
    top: 112px;
    font-family: "Roboto Condensed", sans-serif;
    color: var(--text-light);
    text-align: left;
    text-transform: uppercase;
    line-height: 1.25;
  }
  .pack-info .kind { font-size: 24px; font-weight: 700; }
  .pack-info .size { font-size: 22px; font-weight: 400; text-transform: none; }
  .product-name {
    position: absolute;
    left: 60px;
    top: 392px;
    font-family: "Oswald", sans-serif;
    font-weight: 600;
    font-size: 74px;
    line-height: 1;
    color: var(--green);
  }
  .product-claim {
    position: absolute;
    left: 60px;
    top: 492px;
    width: 360px;
    font-family: "Roboto Condensed", sans-serif;
    font-weight: 700;
    font-size: 31px;
    line-height: 1.2;
    color: var(--grey);
  }
  .quality-badge {
    position: absolute;
    left: 50px;
    top: 690px;
    width: 150px;
    height: 150px;
    border-radius: 50%;
    background: var(--badge);
  }
  .heart-illustration {
    position: absolute;
    left: 395px;
    top: 585px;
    width: 330px;
    height: 330px;
    border-radius: 50%;
    border: 10px solid var(--orange);
    background: radial-gradient(circle at 50% 55%, var(--illus-red) 0%, #7a2a1e 22%, var(--illus-dark) 55%, #15171a 100%);
  }
</style>
</head>
<body>
<main class="canvas">
  <section class="label">
    <svg class="label-swoosh" viewBox="0 0 760 980" aria-hidden="true">
      <path d="M470 0 L760 0 L760 980 L585 980 C690 840 720 650 630 470 C560 330 470 240 470 0 Z" fill="var(--green)"/>
      <path d="M540 0 L760 0 L760 420 C700 300 610 220 540 0 Z" fill="var(--green-deep)" opacity="0.35"/>
      <path d="M445 0 C445 250 540 330 605 470 C695 660 665 850 560 980" fill="none" stroke="var(--orange)" stroke-width="12"/>
    </svg>

    <div class="brand">Plucky Vitamin</div>

    <div class="pack-info">
      <div class="kind">Food Supplement</div>
      <div class="size">1500mg | 60 Tablets</div>
    </div>

    <h1 class="product-name">Heart Health</h1>
    <p class="product-claim">Premium Strength to support Healthy Heart</p>

    <div class="quality-badge" aria-hidden="true"></div>

    <div class="heart-illustration" role="img" aria-label="Illustration of a human torso with a glowing red heart and arteries"></div>
  </section>
</main>
</body>
</html>
```